Create print ready logo with business card and stationery

I have a logo created in Photoshop, but I need it vectorized properly so it can be used for print, outdoor signs etc. The logo should be able to scale between 2 cm and at least 3 meters in width. And to be printed using standard printing methods.

I would also want to have your help in creating business cards and stationery. The company is a school so the design for cards and stationery should be simple and NOT be "cute" just because it is a school. Use the logo and colors provided. I would want originals which I could edit names, positions, phone etc in.

I would want originals in jpg, png, eps, ai, psd and pdf with correct color codes (CMYK, RGB etc) so it can be used for both print and on web. I would want ONE separate file per version of the logo. It's actually just two logos and variations of colors. I want the logos both with and without background boxes (black or white).

```html
<!DOCTYPE html>
<html lang="en">
<head>
<meta charset="utf-8">
<title>Ekbacka Friskola – Business Card</title>
<link rel="stylesheet" href="https://fonts.googleapis.com/css2?family=Jost:wght@400;500;600&display=swap">
<style>
  :root {
    --backdrop: #e8e6e3;
    --card: #ffffff;
    --ink: #3a3a3c;
    --ink-soft: #6b6b6e;
    --rule: #8c8c8f;
    --yellow: #c9b417;
    --orange: #e0722a;
    --blue: #1f7fc0;
    --shadow: rgba(60, 55, 50, 0.18);
  }
  * { box-sizing: border-box; margin: 0; padding: 0; }
  html, body {
    width: 1200px; height: 996px; overflow: hidden;
    background: var(--backdrop);
    font-family: "Jost", "Futura", sans-serif;
    color: var(--ink);
  }
  .sheet {
    position: relative; width: 1200px; height: 996px;
    display: flex; align-items: center; justify-content: center; gap: 48px;
  }
  .card {
    position: relative;
    width: 540px; height: 309px;
    background: var(--card);
    box-shadow: 0 10px 28px var(--shadow), 0 2px 4px var(--shadow);
  }

  /* Front */
  .card--front .wordmark {
    position: absolute; left: 96px; top: 132px;
    display: flex; align-items: center; gap: 14px;
  }
  .wordmark__square {
    width: 12px; height: 12px;
    background: var(--ink);
  }
  .wordmark__name {
    font-weight: 400; font-size: 36px; line-height: 44px;
    letter-spacing: 0.3px; color: var(--ink);
  }

  /* Back */
  .card--back .brand {
    position: absolute; right: 34px; top: 40px;
    display: flex; align-items: center; gap: 8px;
  }
  .brand__square { width: 9px; height: 9px; background: var(--ink); }
  .brand__name {
    font-weight: 500; font-size: 15px; letter-spacing: 0.4px;
    color: var(--ink);
  }

  .contact {
    position: absolute; left: 34px; top: 150px; width: 270px;
  }
  .contact__person {
    padding-bottom: 6px;
    border-bottom: 1px solid var(--rule);
  }
  .contact__name { font-weight: 600; font-size: 16px; line-height: 18px; }
  .contact__role { font-size: 10px; color: var(--ink-soft); letter-spacing: 0.3px; }
  .contact__row {
    display: flex; align-items: center; gap: 10px;
    height: 28px; border-bottom: 1px solid var(--rule);
    font-size: 11.5px; color: var(--ink);
    white-space: nowrap;
  }
  .contact__icon {
    width: 22px; height: 22px; flex: none;
    display: flex; align-items: center; justify-content: center;
  }
  .contact__icon--phone { background: var(--yellow); }
  .contact__icon--mail { background: var(--orange); }
  .contact__icon--pin { background: var(--blue); }
</style>
</head>
<body>
  <main class="sheet">
    <section class="card card--front" aria-label="Card front">
      <div class="wordmark">
        <span class="wordmark__square"></span>
        <p class="wordmark__name">Ekbacka Friskola</p>
      </div>
    </section>

    <section class="card card--back" aria-label="Card back">
      <div class="brand">
        <span class="brand__square"></span>
        <span class="brand__name">Ekbacka Friskola</span>
      </div>

      <div class="contact">
        <div class="contact__person">
          <p class="contact__name">Anders Lind</p>
          <p class="contact__role">Managing Director</p>
        </div>
        <div class="contact__row">
          <span class="contact__icon contact__icon--phone">
            <svg width="12" height="14" viewBox="0 0 12 14" aria-hidden="true">
              <rect x="2" y="1" width="8" height="12" rx="1.5" fill="none" stroke="#fff" stroke-width="1.3"/>
              <line x1="5" y1="10.5" x2="7" y2="10.5" stroke="#fff" stroke-width="1.3"/>
            </svg>
          </span>
          <span>+ 46 (8) 555 0142</span>
        </div>
        <div class="contact__row">
          <span class="contact__icon contact__icon--mail">
            <svg width="14" height="10" viewBox="0 0 14 10" aria-hidden="true">
              <rect x="1" y="1" width="12" height="8" fill="none" stroke="#fff" stroke-width="1.2"/>
              <polyline points="1,1 7,6 13,1" fill="none" stroke="#fff" stroke-width="1.2"/>
            </svg>
          </span>
          <span>anders.lind@ekbackaskola</span>
        </div>
        <div class="contact__row">
          <span class="contact__icon contact__icon--pin">
            <svg width="12" height="14" viewBox="0 0 12 14" aria-hidden="true">
              <path d="M6 13 C3 9 1.5 7 1.5 5 A4.5 4.5 0 0 1 10.5 5 C10.5 7 9 9 6 13 Z" fill="none" stroke="#fff" stroke-width="1.2"/>
              <circle cx="6" cy="5" r="1.6" fill="#fff"/>
            </svg>
          </span>
          <span>42 Lindgatan Uppsala</span>
        </div>
      </div>
    </section>
  </main>
</body>
</html>
```